business card for make-up artist

I want an upscale looking business card to promote my business. I am a make up artist/hair stylist.
I want to use the words "Velvet Hour" as the name of my business. I'm not sure of a good tag line to go under that, so any suggestions are welcomed. If there are different styles instead of just using the same kind of normal shape business card i am open to that as well.
I like the font that is seen on Mirabel Journal.
My Name is Tessa Brantwood
my phone number is 418-305-7826
Pictora: the.velvet.hour

Industry/Entity Type

Hair And Beauty

Contact Information for Business Card

Name of Business: Velvet Hour
Licensed Cosmetologist Tessa Brantwood
418-305-7826

Font styles to use
Serif

Requirements
Must have
• I want an chic style business card. I love gold letters and maybe a black background. I like the font that is used in Mirabel Journal for their name Mirabel.
• FONT!! I LOVE the font called Onyx, Cheddar Jack, and Daydreamer that you can see an example on typeharbor.com
Should not have
• Cartoon characters

```html
<!DOCTYPE html>
<html lang="en">
<head>
<meta charset="utf-8">
<title>Velvet Hour – Business Card</title>
<link href="https://fonts.googleapis.com/css2?family=Six+Caps&family=Nothing+You+Could+Do&display=swap" rel="stylesheet">
<style>
  :root {
    --ink: #000000;
    --mist: #e9e8e6;
    --gold-light: #f4e3b5;
    --gold: #c9a968;
    --gold-deep: #8d6f3a;
    --branch: rgba(201, 169, 104, 0.22);
  }
  html, body {
    margin: 0;
    padding: 0;
    overflow: hidden;
    background: #ffffff;
  }
  .card {
    position: relative;
    width: 750px;
    height: 1200px;
    overflow: hidden;
    background: linear-gradient(to bottom, var(--ink) 0%, #050505 52%, #3a3a3a 72%, #9c9c9c 88%, var(--mist) 100%);
  }
  .branches {
    position: absolute;
    inset: 0;
    background:
      radial-gradient(ellipse 55% 30% at 75% 28%, var(--branch), transparent 70%),
      radial-gradient(ellipse 45% 22% at 20% 38%, rgba(201,169,104,0.14), transparent 70%),
      radial-gradient(ellipse 70% 25% at 55% 93%, rgba(168,140,90,0.35), transparent 70%),
      radial-gradient(ellipse 40% 20% at 90% 62%, rgba(201,169,104,0.16), transparent 70%);
  }
  .gold {
    background: linear-gradient(to bottom, var(--gold-light) 0%, var(--gold) 45%, var(--gold-deep) 70%, var(--gold-light) 100%);
    -webkit-background-clip: text;
    background-clip: text;
    color: transparent;
  }
  .brand-name {
    position: absolute;
    top: 30px;
    left: 0;
    width: 750px;
    margin: 0;
    text-align: center;
    white-space: nowrap;
    font-family: "Six Caps", sans-serif;
    font-weight: 400;
    font-size: 262px;
    line-height: 1;
    letter-spacing: 4px;
  }
  .owner {
    position: absolute;
    top: 285px;
    left: 0;
    width: 750px;
    text-align: center;
    font-family: "Nothing You Could Do", cursive;
    color: var(--gold);
  }
  .owner-name {
    display: block;
    font-size: 54px;
    line-height: 1.2;
  }
  .owner-title {
    display: block;
    font-size: 56px;
    line-height: 1.2;
    color: var(--gold-light);
  }
  .contact {
    position: absolute;
    left: 55px;
    top: 605px;
    margin: 0;
    padding: 0;
    list-style: none;
  }
  .contact-row {
    display: flex;
    align-items: baseline;
    gap: 18px;
    height: 112px;
  }
  .contact-label {
    font-family: "Six Caps", sans-serif;
    font-size: 118px;
    line-height: 1;
    letter-spacing: 2px;
  }
  .contact-value {
    font-family: "Nothing You Could Do", cursive;
    font-size: 44px;
    color: var(--gold-light);
  }
</style>
</head>
<body>
  <div class="card">
    <div class="branches" role="img" aria-label="Gold tree branches with small birds spreading across the card, a tree silhouette at the bottom"></div>

    <h1 class="brand-name gold">VELVET HOUR</h1>

    <div class="owner">
      <span class="owner-name">Tessa Brantwood</span>
      <span class="owner-title">Licensed Cosmetologist</span>
    </div>

    <ul class="contact">
      <li class="contact-row">
        <span class="contact-label gold">PHONE</span>
        <span class="contact-value">(418) 305 . 7826</span>
      </li>
      <li class="contact-row">
        <span class="contact-label gold">PICTORA</span>
        <span class="contact-value">the.velvet.hour</span>
      </li>
    </ul>
  </div>
</body>
</html>
```